Website design for recruitment solutions

We connect top talents to fast growing employers in Asia. We need to revamp our existing website (currently outdated) and also add more pages to make it more informative for talents and employers.
We need final design output to be for both desktop and mobile devices. The final design output must come with all specifications so it's easier for our dev team to implement. We have a detailed mockup but we expect the design to be significantly changed by the final output. We want the pages to look aesthetic, modern and professional.
Number of Pages Required
5+ page
Requirements
Must have
- - To have Pages design for desktop+mobile. Need to take into account intermediate resolutions like 1365px\1023px\767px\479px, especially if mobile/desktop design differs considerably. Design should be repeatable (between pages), suitable for block-layout.
Nice to have
- In terms of receiving files, we usually work with designers who can deliver files in Figma or Sketch with export to Figma. If in PSD format - please export to Zeplin or Avocode, otherwise will be difficult to open

```html
<!DOCTYPE html>
<html lang="en">
<head>
<meta charset="utf-8">
<title>HIRELANE – How we work</title>
<link href="https://fonts.googleapis.com/css2?family=Roboto:wght@400;500;700&display=swap" rel="stylesheet">
<style>
:root{
  --navy:#55739b;
  --navy-dark:#4a6689;
  --red:#f41515;
  --mint:#c4e9d7;
  --green:#5cc58f;
  --page:#f8f8f8;
  --white:#ffffff;
  --answer:#e2e8ef;
  --ink:#333a44;
  --footer-text:#b7c6dc;
}
*{margin:0;padding:0;box-sizing:border-box}
html,body{width:1004px;height:1200px;overflow:hidden}
body{position:relative;background:var(--page);font-family:'Roboto',sans-serif;color:var(--ink)}
.abs{position:absolute}

/* hero */
.hero{position:absolute;left:0;top:0;width:1004px;height:224px}
.hero svg{display:block}
.hero-title{position:absolute;left:0;top:92px;width:1004px;text-align:center;color:var(--white);font-weight:700;font-size:27px;line-height:33px;padding-left:4px}
.hero-title .accent{color:var(--red)}

/* nav */
.nav{position:absolute;left:211px;top:0;width:581px;height:33px;background:var(--navy);border-radius:0 0 16px 16px;box-shadow:0 3px 8px rgba(0,0,0,.15)}
.brand{position:absolute;font-weight:700;letter-spacing:1px;color:#b8cbe6}
.nav .brand{left:16px;top:10px;font-size:12px}
.nav-link{position:absolute;top:12px;font-size:6.5px;color:var(--white)}
.nav-link.active::after{content:"";position:absolute;left:-1px;right:-1px;top:20px;height:1.5px;background:var(--red)}
.nav-divider{position:absolute;left:467px;top:12px;width:1px;height:9px;background:var(--white)}
.btn{position:absolute;background:var(--red);color:var(--white);border-radius:9px;font-size:6.5px;display:flex;align-items:center;justify-content:center;gap:2px;box-shadow:0 2px 4px rgba(0,0,0,.15)}

/* step cards */
.card{position:absolute;top:309px;width:134px;height:186px;background:var(--white);border-radius:20px;box-shadow:0 3px 8px rgba(0,0,0,.08)}
.badge{position:absolute;left:0;top:-45px;width:90px;height:90px;border-radius:50%;background:var(--white);box-shadow:0 1px 4px rgba(0,0,0,.1);display:flex;align-items:center;justify-content:center}
.badge-inner{width:81px;height:81px;border-radius:50%;background:var(--mint);display:flex;align-items:center;justify-content:center}
.card h3{position:absolute;left:6px;top:62px;font-size:10.5px;font-weight:700;color:var(--navy)}
.card .rule{position:absolute;left:6px;top:84px;width:57px;height:1.2px;background:var(--red)}
.card p{position:absolute;left:6px;top:104px;width:124px;font-size:7.5px;line-height:9.4px}

/* empower */
.section-title{position:absolute;left:0;width:1004px;text-align:center;font-weight:700;font-size:19.5px;color:var(--navy)}
.section-sub{position:absolute;left:0;top:585px;width:1004px;text-align:center;font-size:7.5px;line-height:9.4px}
.center-rule{position:absolute;left:474px;top:618px;width:56px;height:1.2px;background:var(--red)}
.timeline{position:absolute;left:236px;top:671px;width:1.5px;height:122px;background:var(--green)}
.dot{position:absolute;left:232px;width:10px;height:10px;border-radius:50%;background:var(--green);border:1.5px solid var(--white);box-shadow:0 1px 2px rgba(0,0,0,.15)}
.question{position:absolute;left:262px;width:183px;height:31px;background:var(--white);border-radius:16px;box-shadow:0 2px 5px rgba(0,0,0,.1);font-weight:700;font-size:10.5px;color:var(--navy);padding:9px 11px}
.answer{position:absolute;left:462px;width:329px;height:31px;background:var(--answer);border-radius:16px;box-shadow:0 2px 5px rgba(0,0,0,.06);font-size:7.5px;line-height:9.4px;padding:6px 15px}

/* cta */
.cta{left:467px;top:908px;width:70px;height:15px;border-radius:8px}

/* footer */
.footer{position:absolute;left:0;top:975px;width:1004px;height:225px}
.footer-bg{position:absolute;left:0;top:0}
.footer .brand{left:212px;top:67px;font-size:12px}
.footer h4{position:absolute;top:67px;font-size:10px;font-weight:500;color:var(--white)}
.footer-text{position:absolute;font-size:7px;line-height:9px;color:var(--footer-text)}
.social{position:absolute;top:112px;width:16px;height:16px;border-radius:50%;background:var(--white)}
.footer-rule{position:absolute;left:212px;top:181px;width:580px;height:1px;background:#8ea3c1}
.legal{position:absolute;top:192px;font-size:6px;line-height:7.5px;color:var(--white)}
</style>
</head>
<body>

<header class="hero">
  <svg width="1004" height="224" role="img" aria-label="Aerial photograph of a riverside city skyline with hills, tinted blue-grey">
    <defs>
      <linearGradient id="heroTone" x1="0" y1="0" x2="0" y2="1">
        <stop offset="0" stop-color="#6f7f8c"/>
        <stop offset=".55" stop-color="#5d6063"/>
        <stop offset="1" stop-color="#7a6456"/>
      </linearGradient>
    </defs>
    <path d="M0 0H1004V171C880 180 720 222 502 222C290 222 140 175 0 171Z" fill="url(#heroTone)"/>
  </svg>
  <h1 class="hero-title"><span class="accent">Maximum Transparency</span> And Feedback<br>Throughout The Process</h1>
</header>

<nav class="nav">
  <div class="brand">HIRELANE</div>
  <span class="nav-link" style="left:224px">Home</span>
  <span class="nav-link active" style="left:262px">How we work</span>
  <span class="nav-link" style="left:313px">Browse jobs</span>
  <span class="nav-link" style="left:365px">Employers</span>
  <span class="nav-link" style="left:416px">About us</span>
  <span class="nav-divider"></span>
  <span class="nav-link" style="left:484px">&#9711; Login</span>
  <span class="btn" style="left:516px;top:9px;width:49px;height:15px">Register</span>
</nav>

<section>
  <article class="card" style="left:211px">
    <div class="badge"><div class="badge-inner">
      <svg width="46" height="40" viewBox="0 0 46 40"><path d="M2 10H14A6 6 0 1 1 24 10H32V18A6 6 0 1 1 32 28V38H22A6 6 0 1 0 12 38H2Z" fill="var(--green)"/></svg>
    </div></div>
    <h3>01. Matching</h3><span class="rule"></span>
    <p>Once registered, our matching algorithms identify any potential roles real time. Our recruiters review the quality of matches before sending them to you.</p>
  </article>
  <article class="card" style="left:359px">
    <div class="badge"><div class="badge-inner">
      <svg width="46" height="38" viewBox="0 0 46 38" fill="none" stroke="var(--green)" stroke-width="3.5" stroke-linejoin="round"><path d="M4 14C4 7 11 3 18 3S32 7 32 14S25 25 18 25C15 25 13 24 11 24L4 28L6 21C5 19 4 17 4 14Z"/><path d="M34 11C39 13 42 17 42 21C42 24 41 26 40 27L42 34L35 31C33 32 31 32 29 32C24 32 20 30 18 27"/></svg>
    </div></div>
    <h3>02. Role briefing</h3><span class="rule"></span>
    <p>Our recruiters will jump on a call with you to explain more about the role. This is also when we get to learn more about you and your career aspirations.</p>
  </article>
  <article class="card" style="left:507px">
    <div class="badge"><div class="badge-inner">
      <svg width="40" height="40" viewBox="0 0 40 40" fill="none" stroke="var(--green)" stroke-width="3.5" stroke-linecap="round" stroke-linejoin="round"><circle cx="20" cy="20" r="17"/><path d="M12 21L18 27L28 14"/></svg>
    </div></div>
    <h3>03. Submit &amp; interview</h3><span class="rule"></span>
    <p>After we have received your approval to apply, we handle the profile submission and any interview logistics. Our recruiters provide prep as you progress through each interview round.</p>
  </article>
  <article class="card" style="left:655px">
    <div class="badge"><div class="badge-inner">
      <svg width="42" height="42" viewBox="0 0 42 42" fill="none" stroke="var(--green)" stroke-width="3.5" stroke-linejoin="round"><path d="M39 3L3 20L16 25L22 39Z"/><path d="M39 3L16 25"/></svg>
    </div></div>
    <h3>04. Offering</h3><span class="rule"></span>
    <p>You have our full support during from navigating difficult conversations, salary negotiation, to understanding how this opportunity fits your long term career goals.</p>
  </article>
</section>

<section>
  <h2 class="section-title" style="top:556px">We empower talents to make informed career decisions</h2>
  <p class="section-sub">Every intel that we gather is dissected and organized in a way so that we<br>facilitate the right intel at the right time</p>
  <span class="center-rule"></span>

  <span class="timeline"></span>
  <span class="dot" style="top:666px"></span>
  <span class="dot" style="top:707px"></span>
  <span class="dot" style="top:747px"></span>
  <span class="dot" style="top:788px"></span>

  <div class="question" style="top:655px">Which opportunities to look at?</div>
  <div class="answer" style="top:655px">We curate roles that are relevant to your profile and interests.</div>
  <div class="question" style="top:696px">Why should I apply?</div>
  <div class="answer" style="top:696px">We demystify the role and the company and help to make the connection.</div>
  <div class="question" style="top:736px">How can I enhance my chances?</div>
  <div class="answer" style="top:736px">We share intel on the function/team set up and hiring process. We help strategize your candidacy for each round.</div>
  <div class="question" style="top:777px">What shall I do with this offer?</div>
  <div class="answer" style="top:777px">We review various decision factors including the role's progression, learning opportunities, stability and compensation.</div>
</section>

<section>
  <h2 class="section-title" style="top:855px">Ready to join us?</h2>
  <span class="btn cta">Get started &#10140;</span>
</section>

<footer class="footer">
  <svg class="footer-bg" width="1004" height="225"><path d="M0 56C160 40 330 6 502 6S850 40 1004 56V225H0Z" fill="var(--navy)"/></svg>
  <div class="brand">HIRELANE</div>
  <h4 style="left:405px">Talents</h4>
  <h4 style="left:493px">Employers</h4>
  <h4 style="left:580px">About us</h4>
  <h4 style="left:666px">Connect with us</h4>
  <p class="footer-text" style="left:212px;top:113px;width:165px">HIRELANE is a modern recruitment partner for high potential technology and finance talents. We work closely with hedge funds, systematic trading Fin Tech employers experiencing hyper growth in Asia</p>
  <p class="footer-text" style="left:405px;top:113px">How we work<br>Browse jobs</p>
  <p class="footer-text" style="left:493px;top:113px">Why HIRELANE</p>
  <p class="footer-text" style="left:580px;top:113px">About HIRELANE<br>Working at HIRELANE</p>
  <span class="social" style="left:666px"></span>
  <span class="social" style="left:692px"></span>
  <span class="social" style="left:718px"></span>
  <span class="btn" style="left:744px;top:112px;width:46px;height:15px">Register</span>
  <span class="footer-rule"></span>
  <p class="legal" style="left:212px">@HIRELANE 2012-2020 All rights reserved.</p>
  <p class="legal" style="left:405px;width:180px">Harbour Gate Partners Limited (EA License No. 00000) Suite 12, Level 5, Lantern Tower, 88 Harbourview Road, Hong Kong</p>
  <p class="legal" style="left:599px;width:180px">Hirelane Pte. Ltd. (License No. 00A0000) 42 Meridian Street, #10-02 Meridian House, Singapore 000000</p>
</footer>

</body>
</html>
```